Outdoor kitchen and Appliance Need new business card

We need a new business card, for our business.

Front side with all info, back side with more brand identity.

I have attached some drafts, we moved up but it lacks creativity.

Use https://photos.quendrix.com and I can purchase, the stock photo and send it you if you design is chosen.

We are also planing on printing business card with the logo, having a spot uv. I have attached instructions.

Plumtarvessa.com is our website

Target Market(s)

Extremely high end customer.

Contact Information for Business Card

Double sided with spot uv on logos

Colors
ec1f27

Requirements
Must have
• See sample I have attached, we are open to ideas.

Colors, are: RED, Stainless steel, Black

```html
<!DOCTYPE html>
<html lang="en">
<head>
<meta charset="utf-8">
<title>Plumtarvessa — Business Card</title>
<link rel="stylesheet" href="https://fonts.googleapis.com/css2?family=Roboto:wght@400;500;700&display=swap">
<style>
  :root {
    --bg-light: #d2d2d2;
    --bg-dark: #a3a3a3;
    --card: #141416;
    --red: #ec1f27;
    --steel: #a9a9ad;
    --white: #f2f2f2;
    --gloss: #2b2b2f;
  }
  * { box-sizing: border-box; margin: 0; padding: 0; }
  html, body { width: 1200px; height: 801px; overflow: hidden; }
  body {
    background: linear-gradient(180deg, var(--bg-light), var(--bg-dark));
    font-family: "Roboto", Arial, sans-serif;
    display: flex;
    align-items: center;
    justify-content: center;
    gap: 40px;
  }
  .card {
    position: relative;
    width: 530px;
    height: 303px;
    background: var(--card);
    border-radius: 20px;
    box-shadow: 0 10px 24px rgba(0,0,0,.35);
    overflow: hidden;
  }
  /* Front */
  .divider {
    position: absolute;
    left: 30px; right: 30px; top: 170px;
    height: 1px;
    background: var(--red);
  }
  .brand-name {
    position: absolute;
    right: 34px; top: 72px;
    display: flex; align-items: center; gap: 8px;
    font-size: 24px; font-weight: 700;
    letter-spacing: 1px;
    color: var(--steel);
    text-transform: uppercase;
  }
  .brand-mark {
    width: 14px; height: 14px;
    border: 2px solid var(--steel);
  }
  .person {
    position: absolute;
    left: 34px; bottom: 145px;
  }
  .person-name {
    color: var(--red);
    font-size: 24px; font-weight: 700;
    letter-spacing: .5px;
    text-transform: uppercase;
    line-height: 1.1;
  }
  .person-title {
    color: var(--white);
    font-size: 14px;
    margin-top: 3px;
  }
  .contacts {
    position: absolute;
    left: 34px; top: 182px;
    list-style: none;
    color: var(--white);
    font-size: 14px;
    line-height: 20px;
  }
  .contacts li { display: flex; align-items: center; gap: 8px; }
  .contacts svg { width: 11px; height: 11px; fill: var(--red); flex: none; }
  .contacts .label { color: var(--red); font-size: 12px; }
  .address {
    position: absolute;
    left: 340px; top: 182px;
    color: var(--white);
    font-size: 13px;
    line-height: 18px;
  }
  .address-heading {
    color: var(--red);
    font-weight: 500;
    text-transform: uppercase;
  }
  /* Back */
  .card-back { display: flex; align-items: center; justify-content: center; }
  .back-brand {
    font-size: 40px; font-weight: 700;
    letter-spacing: 2px;
    color: var(--gloss);
    text-transform: uppercase;
  }
</style>
</head>
<body>
  <section class="card card-front">
    <div class="brand-name"><span class="brand-mark"></span>Plumtarvessa</div>

    <div class="person">
      <div class="person-name">Marco Vellini</div>
      <div class="person-title">Sales Manager</div>
    </div>

    <div class="divider"></div>

    <ul class="contacts">
      <li>
        <svg viewBox="0 0 12 12"><path d="M3 0h6a1 1 0 0 1 1 1v10a1 1 0 0 1-1 1H3a1 1 0 0 1-1-1V1a1 1 0 0 1 1-1zm0 1.5v8h6v-8z"/></svg>
        <span>(555)201-4837 <span class="label">(Cell)</span></span>
      </li>
      <li>
        <svg viewBox="0 0 12 12"><path d="M2.5 0.5l2 2.5-1.2 1.5c.8 1.7 2.1 3 3.7 3.8L8.5 7l2.5 2-1 2.5C5.5 11.5 0.5 6.5 0.5 2z"/></svg>
        <span>(555)318-6620 <span class="label">(Office)</span></span>
      </li>
      <li>
        <svg viewBox="0 0 12 12"><path d="M3 0h6v3H3zM1 4h10a1 1 0 0 1 1 1v4H10v3H2V9H0V5a1 1 0 0 1 1-1zm2 5v2h6V9z"/></svg>
        <span>(555)472-9051</span>
      </li>
      <li>
        <svg viewBox="0 0 12 12"><path d="M0 2h12v8H0zm1 1v.4l5 3.3 5-3.3V3z"/></svg>
        <span>Marco@Plumtarvessa.com</span>
      </li>
      <li>
        <svg viewBox="0 0 12 12"><path d="M6 0a6 6 0 1 0 0 12A6 6 0 0 0 6 0zm0 1.2a4.8 4.8 0 0 1 0 9.6A4.8 4.8 0 0 1 6 1.2zM1.5 6h9M6 1.5v9" stroke="#ec1f27" stroke-width="1"/></svg>
        <span>www.Plumtarvessa.com</span>
      </li>
    </ul>

    <div class="address">
      <div class="address-heading">Office - Showroom</div>
      <div>4480 Larkspur Way Suite 12</div>
      <div>Coral Fenwick, FL 33990</div>
    </div>
  </section>

  <section class="card card-back">
    <div class="back-brand">Plumtarvessa</div>
  </section>
</body>
</html>
```